KB Rubbish Removal Business Card

Hey,
I need a double sided business card designed for a rubbish removal business based in Australia. Logo is already chosen, similar colours preferred for both sides of the business card.

Details to include:

Front:

KB Rubbish Removal
Darren Holloway
Managing Director
Mobile: 0471 902 146
Email: darren@kbrubbishremoval.com.au
Website: kbrubbishremoval.com.au

Rear:

How did we do?
kbrubbishremoval.com.au/review

```html
<!DOCTYPE html>
<html lang="en">
<head>
<meta charset="utf-8">
<title>KB Rubbish Removal – Business Card</title>
<link rel="stylesheet" href="https://fonts.googleapis.com/css2?family=Josefin+Sans:wght@300;400;600;700&display=swap">
<style>
  :root {
    --page-bg: #d4d4d4;
    --card-white: #ffffff;
    --green-dark: #0f8a3a;
    --green-mid: #22a447;
    --green-light: #5cc34a;
    --green-pale: #8fd866;
    --name-green: #2f8a45;
    --title-grey: #8a8a8a;
    --contact-lime: #cde94e;
    --text-white: #ffffff;
  }
  * { box-sizing: border-box; margin: 0; padding: 0; }
  html, body {
    width: 1200px; height: 800px; overflow: hidden;
    background: var(--page-bg);
    font-family: "Josefin Sans", sans-serif;
  }
  .canvas {
    width: 1200px; height: 800px;
    display: flex; align-items: center; justify-content: center; gap: 50px;
  }
  .card {
    position: relative; width: 525px; height: 300px;
    background: var(--card-white); overflow: hidden;
    box-shadow: 0 6px 18px rgba(0,0,0,0.18);
  }
  .card-shapes { position: absolute; inset: 0; width: 100%; height: 100%; }

  /* Rear */
  .rear-content {
    position: absolute; inset: 0;
    display: flex; flex-direction: column; align-items: center; justify-content: center;
    color: var(--name-green); text-align: center;
  }
  .rear-heading { font-size: 25px; font-weight: 400; letter-spacing: 1px; margin-bottom: 8px; }
  .rear-url { font-size: 21px; font-weight: 400; }
  .rear-stars { font-size: 14px; letter-spacing: 4px; margin-top: 10px; color: var(--green-dark); }

  /* Front */
  .brand-mark {
    position: absolute; top: 20px; right: 24px;
    display: flex; align-items: center; gap: 6px;
    color: var(--green-mid); font-size: 11px; font-weight: 600;
  }
  .brand-dot { width: 14px; height: 14px; border-radius: 50%; background: var(--green-mid); }
  .person { position: absolute; top: 74px; left: 150px; text-align: right; }
  .person-name { font-size: 25px; font-weight: 400; color: var(--name-green); letter-spacing: 0.5px; white-space: nowrap; }
  .person-title {
    font-size: 10px; font-weight: 400; color: var(--title-grey);
    letter-spacing: 3px; text-transform: uppercase; margin-top: 3px; white-space: nowrap;
  }
  .company {
    position: absolute; left: 28px; top: 200px;
    color: var(--text-white); font-size: 14px; font-weight: 700;
    letter-spacing: 3px; text-transform: uppercase;
  }
  .contact-list { position: absolute; left: 28px; top: 224px; list-style: none; }
  .contact-item {
    display: flex; align-items: center; gap: 8px;
    color: var(--contact-lime); font-size: 11.5px; font-weight: 400; line-height: 19px;
  }
  .contact-icon { width: 11px; height: 11px; flex: none; }
</style>
</head>
<body>
<main class="canvas">

  <section class="card card-rear" aria-label="Business card rear">
    <svg class="card-shapes" viewBox="0 0 525 300" preserveAspectRatio="none" aria-hidden="true">
      <path d="M375,0 A72,72 0 0 0 519,0 Z" fill="var(--green-light)"/>
      <path d="M0,300 L0,235 C40,205 95,195 140,222 C170,240 200,270 225,300 Z" fill="var(--green-mid)"/>
      <path d="M0,300 L0,258 C45,232 90,232 130,262 C150,278 165,292 170,300 Z" fill="var(--green-dark)" opacity="0.55"/>
    </svg>
    <div class="rear-content">
      <h2 class="rear-heading">HOW DID WE DO?</h2>
      <p class="rear-url">kbrubbishremoval.com.au/review</p>
      <p class="rear-stars" aria-label="Five stars">★★★★★</p>
    </div>
  </section>

  <section class="card card-front" aria-label="Business card front">
    <svg class="card-shapes" viewBox="0 0 525 300" preserveAspectRatio="none" aria-hidden="true">
      <path d="M0,135 C110,190 240,205 330,162 C410,122 470,78 525,58 L525,300 L0,300 Z" fill="var(--green-dark)"/>
      <path d="M400,300 C435,220 472,145 525,100 L525,300 Z" fill="var(--green-light)"/>
      <path d="M400,300 C435,220 472,145 525,100 L525,114 C478,158 442,228 413,300 Z" fill="var(--green-pale)"/>
    </svg>

    <div class="brand-mark"><span class="brand-dot"></span>KB Rubbish Removal</div>

    <div class="person">
      <h1 class="person-name">Darren Holloway</h1>
      <p class="person-title">Managing Director</p>
    </div>

    <p class="company">KB Rubbish Removal</p>
    <ul class="contact-list">
      <li class="contact-item">
        <svg class="contact-icon" viewBox="0 0 24 24"><path fill="var(--contact-lime)" d="M6.6 10.8a15.1 15.1 0 0 0 6.6 6.6l2.2-2.2a1 1 0 0 1 1-.25 11.4 11.4 0 0 0 3.6.57 1 1 0 0 1 1 1V20a1 1 0 0 1-1 1A17 17 0 0 1 3 4a1 1 0 0 1 1-1h3.5a1 1 0 0 1 1 1c0 1.25.2 2.45.57 3.57a1 1 0 0 1-.25 1z"/></svg>
        0471 902 146
      </li>
      <li class="contact-item">
        <svg class="contact-icon" viewBox="0 0 24 24"><rect x="2" y="5" width="20" height="14" fill="var(--contact-lime)"/><path d="M2 5l10 8 10-8" fill="none" stroke="var(--green-dark)" stroke-width="2"/></svg>
        darren@kbrubbishremoval.com.au
      </li>
      <li class="contact-item">
        <svg class="contact-icon" viewBox="0 0 24 24"><circle cx="12" cy="12" r="10" fill="var(--contact-lime)"/><path d="M2 12h20M12 2c3 3 3 17 0 20M12 2c-3 3-3 17 0 20" fill="none" stroke="var(--green-dark)" stroke-width="1.5"/></svg>
        kbrubbishremoval.com.au
      </li>
    </ul>
  </section>

</main>
</body>
</html>
```